KU Curiosities

We need a web design for an ecommerce website that sells innovative gadgets. ***We are in the early stages of the business and don't have official products yet, they are being created. so we need to use placeholders and fake content, please email me with any questions regarding this.

The web page must look modern, fresh and simple and include-

• Logo
• My Account & View Cart link
• Menu - Home, Shop, The Latest, About Us, FAQ, Blog, Contact Us
• Promo bar at the top of the page like on: http://www.plumandwren.example/plwr/ (you can use placeholder text for now)
• Search Box
• Chatterpage, Chirpline, Vidstream, Clipboardly and Orbnet+ icons
• Slogan “Amaze your friends”
• Free shipping on orders over $50
• Banner section - for now you can highlight one of the fake products below, focus on free shipping on order over $50 or some kind of fake promotion
• New Arrivals section - highlight these fake products since we don't have products yet so you can use these products as place holders-
1. https://www.brisketbay.example/tech-gadgets/the-vorntap
2. https://www.brisketbay.example/tech-gadgets/lobelatch-earbud-securer
3. https://www.brisketbay.example/tech-gadgets/pestavo-headfoams
• credit card logos
• paytrellis.example seal - https://check.paytrellis.example/ptseal/images/secure90x72.gif

Example websites:
http://www.plumandwren.example/plwr/
https://www.brisketbay.example/
http://www.tinmantles.example/
https://sproutwell.example/
http://zevrodesk.example/
http://www.dallowsco.example/
http://www.vistaframe.example/

Requirements
Must have
• • Logo
• Search Box
• credit card logos

```html
<!DOCTYPE html>
<html lang="en">
<head>
<meta charset="utf-8">
<title>KU Curiosities</title>
<link rel="stylesheet" href="https://fonts.googleapis.com/css2?family=Open+Sans:wght@400;600;700&family=Oswald:wght@400;500&display=swap">
<style>
:root{
  --navy:#0f2a5c;
  --navy-deep:#0b2350;
  --blue:#3aa8dc;
  --sky:#4aaee0;
  --ink:#333;
  --muted:#777;
  --line:#e3e3e3;
  --dark:#1f1f1f;
  --darker:#141414;
  --white:#fff;
}
*{box-sizing:border-box;margin:0;padding:0}
html,body{width:900px;height:1200px;overflow:hidden;background:var(--white)}
body{position:relative;font-family:"Open Sans",Arial,sans-serif;color:var(--ink)}
.abs{position:absolute}
.promo-bar{left:0;top:0;width:900px;height:27px;background:var(--navy);color:var(--white);font:400 10px/27px Arial,sans-serif;text-align:center}
.cart-summary{left:89px;top:64px;font-size:11px;color:#444;display:flex;align-items:center;gap:6px}
.brand{left:370px;top:40px;width:160px;text-align:center}
.brand-mark{width:40px;height:40px;border-radius:50%;background:var(--blue);margin:0 auto 6px}
.brand-name{font:700 17px/1 "Open Sans",sans-serif;color:var(--navy)}
.search{left:635px;top:50px;width:175px;height:27px;border:1px solid #ddd;border-radius:14px;box-shadow:0 1px 2px rgba(0,0,0,.1);font-size:10px;color:#999;padding:6px 12px}
.search svg{position:absolute;right:10px;top:6px}
.account-links{left:688px;top:88px;font-size:10px;color:#555;word-spacing:2px}
.main-nav{left:90px;top:116px;width:720px;height:42px;border-top:1px solid var(--line);border-bottom:4px solid #3a3a3a;display:flex;justify-content:space-between;align-items:center;font-size:11.5px;color:#555;padding:0 20px 0 23px}
.main-nav .active{color:var(--blue);font-weight:600}
.nav-underline{left:90px;top:154px;width:79px;height:4px;background:var(--blue)}
.hero{left:90px;top:166px;width:525px;height:311px;background:linear-gradient(90deg,#dfeef8,#f3f7fa 70%,#d6ecf9)}
.hero-photo{left:90px;top:166px;width:395px;height:298px;background:linear-gradient(160deg,#7fd3e0,#3a4a5e 40%,#d9e6ee)}
.hero-product{left:450px;top:245px;width:124px;height:115px;background:linear-gradient(#fff,#f5e6e6)}
.hero-tag{left:90px;top:243px;width:204px;height:186px}
.hero-tag .top{height:90px;background:rgba(18,45,100,.88);color:#fff;font:500 16px/90px Oswald,sans-serif;text-align:center}
.hero-tag .bottom{height:96px;background:rgba(12,14,22,.92);color:#fff;text-align:center;padding-top:16px;font-size:12.5px;line-height:17px}
.hero-tag .off{font-style:italic;font-weight:600;font-size:17px;color:#6fc3ee;line-height:22px}
.dots{left:281px;top:463px;display:flex;gap:7px}
.dots span{width:30px;height:30px;border-radius:50%;background:#fff;border:1px solid #ddd;font-size:10px;line-height:28px;text-align:center;color:#333}
.dots .on{background:var(--blue);color:#fff;border-color:var(--blue)}
.side-promo{left:623px;top:166px;width:188px;height:152px;background:linear-gradient(#1a4d8c,#0e2a52)}
.side-promo .txt{position:absolute;left:0;top:72px;width:188px;height:80px;background:rgba(8,16,32,.55);color:#fff;font-size:17px;line-height:26px;padding:0 38px}
.side-promo .txt b{color:#6fc3ee;font-weight:600}
.ship-promo{left:623px;top:326px;width:188px;height:152px;background:var(--sky);color:#fff;text-align:center;font-size:14px;line-height:18px}
.section-title{left:90px;top:505px;font:400 20px/1 Oswald,sans-serif;color:#333}
.section-arrows{left:788px;top:514px}
.section-rule{left:90px;top:543px;width:720px;height:1px;background:var(--line)}
.product{width:164px;top:567px}
.product .photo{height:169px;border:1px solid #ddd;border-bottom:none;background:#fff;position:relative}
.product .photo div{position:absolute;left:37px;top:34px;width:90px;height:100px}
.product .name{height:24px;background:#eee;text-align:center;font-size:12px;line-height:24px;color:#444}
.product .price{text-align:center;margin-top:9px;font:400 13px/1 Oswald,sans-serif;color:var(--navy)}
.product .price s{color:#999;font-size:9.5px;margin-right:3px}
.product .actions{display:flex;margin-top:10px;border:1px solid #ddd;height:30px}
.product .actions span{flex:1;border-left:1px solid #ddd;display:flex;align-items:center;justify-content:center}
.product .actions span:first-child{border-left:none}
.product .actions .buy{background:var(--navy)}
.feature{top:875px;width:159px;height:79px;color:#fff;background:#222;display:flex;align-items:center;padding:0 10px;gap:6px}
.feature.navy{background:var(--navy)}
.feature .body{flex:1;text-align:center;font-size:8.5px;line-height:13px;font-weight:600}
.feature h3{font-size:13px;font-weight:400;text-decoration:underline;margin-bottom:4px;white-space:nowrap}
.newsletter-field{display:flex;margin-top:6px}
.newsletter-field i{flex:1;height:17px;background:#fff}
.newsletter-field b{width:18px;height:17px;background:var(--blue)}
.footer{left:0;top:1000px;width:900px;height:153px;background:var(--dark)}
.foot-col{top:1029px;width:126px;color:#aaa;font-size:9.5px}
.foot-col h4{font:400 11px/1 Oswald,sans-serif;color:#ddd;padding-bottom:7px;border-bottom:1px solid #444;margin-bottom:7px}
.foot-col li{list-style:none;line-height:16.5px}
.foot-col li::before{content:"\2022";margin-right:5px;font-size:7px;vertical-align:2px}
.foot-col.menu li{line-height:12.5px;font-size:8.5px}
.foot-col .hl{color:var(--blue)}
.foot-col.social li::before{content:none}
.foot-col.social li{display:flex;align-items:center;gap:12px}
.foot-col.social li i{width:8px;height:8px;border-radius:50%;background:#bbb;margin-left:5px}
.bottom-bar{left:0;top:1153px;width:900px;height:47px;background:var(--darker);font-size:9.5px;color:#999}
.bottom-bar .copy{position:absolute;left:90px;top:18px}
.bottom-bar .copy span{color:var(--blue)}
.cards{position:absolute;right:122px;top:17px;display:flex;gap:5px}
.cards span{height:14px;padding:0 3px;background:#eee;color:var(--navy);font-size:6.5px;line-height:14px;font-weight:700;white-space:nowrap}
.seal{position:absolute;left:793px;top:12px;width:31px;height:23px;background:#e9e3c8;border-radius:2px}
</style>
</head>
<body>
<div class="abs promo-bar">Lorem ipsum dolor sit amet, consectetur adipiscing elit. Duis sit amet est in orci tempus ultricies. Suspendisse fringilla pulvinar</div>

<div class="abs cart-summary">0 Item(s) - $0.00
  <svg width="12" height="11" viewBox="0 0 12 11"><path d="M0 1h2l2 6h6l2-5H3" fill="none" stroke="#3aa8dc" stroke-width="1.6"/><circle cx="5" cy="9.5" r="1.2" fill="#3aa8dc"/><circle cx="9" cy="9.5" r="1.2" fill="#3aa8dc"/></svg>
</div>

<div class="abs brand"><div class="brand-mark"></div><div class="brand-name">KU Curiosities</div></div>

<div class="abs search">Search
  <svg width="12" height="12" viewBox="0 0 12 12"><circle cx="5" cy="5" r="3.8" fill="none" stroke="#3aa8dc" stroke-width="1.6"/><path d="M8 8l3 3" stroke="#3aa8dc" stroke-width="1.8"/></svg>
</div>
<div class="abs account-links">My Account &nbsp;&nbsp;| &nbsp;&nbsp;View Cart</div>

<nav class="abs main-nav">
  <span class="active">Home</span><span>Shop</span><span>The Latest</span><span>About Us</span><span>FAQ</span><span>Blog</span><span>Contact Us</span>
</nav>
<div class="abs nav-underline"></div>

<div class="abs hero"></div>
<div class="abs hero-photo" role="img" aria-label="Child wearing over-ear headphones"></div>
<div class="abs hero-product" role="img" aria-label="Red foam headphones product shot"></div>
<div class="abs hero-tag">
  <div class="top">AMAZE YOUR FRIENDS</div>
  <div class="bottom"><div class="off">10% Off on Lorem</div>Free shipping on orders<br>over <b>$50</b></div>
</div>
<div class="abs dots"><span class="on">1</span><span>2</span><span>3</span><span>4</span></div>

<div class="abs side-promo" role="img" aria-label="Gadget close-up in blue light">
  <div class="txt"><b>5%</b> on Lorem<br>dolor sit amit</div>
</div>
<div class="abs ship-promo">
  <svg width="80" height="62" viewBox="0 0 80 62" style="margin-top:26px">
    <rect x="1" y="1" width="54" height="44" rx="4" fill="#fff"/>
    <path d="M56 14h12l11 14v17H56z" fill="#fff"/>
    <circle cx="18" cy="50" r="8" fill="#fff" stroke="#4aaee0" stroke-width="4"/>
    <circle cx="64" cy="50" r="8" fill="#fff" stroke="#4aaee0" stroke-width="4"/>
    <text x="5" y="32" font-family="Open Sans,sans-serif" font-weight="700" font-size="19" fill="#4aaee0">FREE</text>
  </svg>
  <div style="margin-top:6px">Free shipping on<br>orders over <b>$50</b></div>
</div>

<h2 class="abs section-title">New Arrivals</h2>
<svg class="abs section-arrows" width="22" height="12" viewBox="0 0 22 12"><path d="M7 1L2 6l5 5M15 1l5 5-5 5" fill="none" stroke="#333" stroke-width="1.8"/></svg>
<div class="abs section-rule"></div>

<div class="abs product" style="left:90px">
  <div class="photo"><div role="img" aria-label="Red clip hook gadget" style="background:linear-gradient(#f2f2f2,#d9d9d9)"></div></div>
  <div class="name">Lorem ipsum dolor</div>
  <div class="price"><s>$160.00</s> $150.00</div>
  <div class="actions">
    <span class="buy"><svg width="11" height="10" viewBox="0 0 12 11"><path d="M0 1h2l2 6h6l2-5H3" fill="none" stroke="#fff" stroke-width="1.6"/><circle cx="5" cy="9.5" r="1.2" fill="#fff"/><circle cx="9" cy="9.5" r="1.2" fill="#fff"/></svg></span>
    <span><svg width="10" height="9" viewBox="0 0 10 9"><path d="M5 9L1 5a2.3 2.3 0 014-3 2.3 2.3 0 014 3z" fill="#ccc"/></svg></span>
    <span><svg width="11" height="9" viewBox="0 0 11 9"><path d="M0 2.5h9M7 0l3 2.5L7 5M11 6.5H2M4 4L1 6.5 4 9" fill="none" stroke="#999" stroke-width="1.3"/></svg></span>
    <span><svg width="11" height="11" viewBox="0 0 11 11"><circle cx="5.5" cy="5.5" r="4.6" fill="none" stroke="#999"/><path d="M4.5 3.5l2 2-2 2" fill="none" stroke="#999"/></svg></span>
  </div>
</div>

<div class="abs product" style="left:275px">
  <div class="photo"><div role="img" aria-label="Blue foam headphones" style="background:linear-gradient(#3a6fe0,#1d3fb0)"></div></div>
  <div class="name">Lorem ipsum dolor</div>
  <div class="price"><s>$160.00</s> $150.00</div>
  <div class="actions">
    <span><svg width="11" height="10" viewBox="0 0 12 11"><path d="M0 1h2l2 6h6l2-5H3" fill="none" stroke="#ccc" stroke-width="1.6"/><circle cx="5" cy="9.5" r="1.2" fill="#ccc"/><circle cx="9" cy="9.5" r="1.2" fill="#ccc"/></svg></span>
    <span><svg width="10" height="9" viewBox="0 0 10 9"><path d="M5 9L1 5a2.3 2.3 0 014-3 2.3 2.3 0 014 3z" fill="#ccc"/></svg></span>
    <span><svg width="11" height="9" viewBox="0 0 11 9"><path d="M0 2.5h9M7 0l3 2.5L7 5M11 6.5H2M4 4L1 6.5 4 9" fill="none" stroke="#999" stroke-width="1.3"/></svg></span>
    <span><svg width="11" height="11" viewBox="0 0 11 11"><circle cx="5.5" cy="5.5" r="4.6" fill="none" stroke="#999"/><path d="M4.5 3.5l2 2-2 2" fill="none" stroke="#999"/></svg></span>
  </div>
</div>

<div class="abs product" style="left:461px">
  <div class="photo"><div role="img" aria-label="Row of earbud securer hooks" style="left:20px;width:126px;background:linear-gradient(90deg,#bbb,#4a6fa0,#a33,#333)"></div></div>
  <div class="name">Lorem ipsum dolor</div>
  <div class="price"><s>$160.00</s> $150.00</div>
  <div class="actions">
    <span><svg width="11" height="10" viewBox="0 0 12 11"><path d="M0 1h2l2 6h6l2-5H3" fill="none" stroke="#ccc" stroke-width="1.6"/><circle cx="5" cy="9.5" r="1.2" fill="#ccc"/><circle cx="9" cy="9.5" r="1.2" fill="#ccc"/></svg></span>
    <span><svg width="10" height="9" viewBox="0 0 10 9"><path d="M5 9L1 5a2.3 2.3 0 014-3 2.3 2.3 0 014 3z" fill="#ccc"/></svg></span>
    <span><svg width="11" height="9" viewBox="0 0 11 9"><path d="M0 2.5h9M7 0l3 2.5L7 5M11 6.5H2M4 4L1 6.5 4 9" fill="none" stroke="#999" stroke-width="1.3"/></svg></span>
    <span><svg width="11" height="11" viewBox="0 0 11 11"><circle cx="5.5" cy="5.5" r="4.6" fill="none" stroke="#999"/><path d="M4.5 3.5l2 2-2 2" fill="none" stroke="#999"/></svg></span>
  </div>
</div>

<div class="abs product" style="left:646px">
  <div class="photo"><div role="img" aria-label="Red foam headphones" style="background:linear-gradient(#e23a3a,#a81c1c)"></div></div>
  <div class="name">Lorem ipsum dolor</div>
  <div class="price"><s>$160.00</s> $150.00</div>
  <div class="actions">
    <span><svg width="11" height="10" viewBox="0 0 12 11"><path d="M0 1h2l2 6h6l2-5H3" fill="none" stroke="#ccc" stroke-width="1.6"/><circle cx="5" cy="9.5" r="1.2" fill="#ccc"/><circle cx="9" cy="9.5" r="1.2" fill="#ccc"/></svg></span>
    <span><svg width="10" height="9" viewBox="0 0 10 9"><path d="M5 9L1 5a2.3 2.3 0 014-3 2.3 2.3 0 014 3z" fill="#ccc"/></svg></span>
    <span><svg width="11" height="9" viewBox="0 0 11 9"><path d="M0 2.5h9M7 0l3 2.5L7 5M11 6.5H2M4 4L1 6.5 4 9" fill="none" stroke="#999" stroke-width="1.3"/></svg></span>
    <span><svg width="11" height="11" viewBox="0 0 11 11"><circle cx="5.5" cy="5.5" r="4.6" fill="none" stroke="#999"/><path d="M4.5 3.5l2 2-2 2" fill="none" stroke="#999"/></svg></span>
  </div>
</div>

<div class="abs feature navy" style="left:90px;padding:0 8px 0 12px">
  <svg width="44" height="28" viewBox="0 0 52 32"><rect x="0" y="2" width="30" height="22" rx="2" fill="#fff"/><path d="M31 9h10l8 8v7H31z" fill="#fff"/><circle cx="11" cy="26" r="5" fill="#fff" stroke="#0f2a5c" stroke-width="3"/><circle cx="41" cy="26" r="5" fill="#fff" stroke="#0f2a5c" stroke-width="3"/></svg>
  <div class="body" style="font-size:12px;line-height:18px;font-weight:400"><h3 style="margin:0">Free Shipping</h3>order<br>over $50</div>
</div>
<div class="abs feature" style="left:277px">
  <svg width="32" height="34" viewBox="0 0 32 34"><path d="M5 20v-6a11 11 0 0122 0v6" fill="none" stroke="#fff" stroke-width="2"/><rect x="3" y="18" width="6" height="10" rx="2" fill="#fff"/><rect x="23" y="18" width="6" height="10" rx="2" fill="#fff"/><path d="M26 28c0 4-5 4-9 4" fill="none" stroke="#fff" stroke-width="1.5"/></svg>
  <div class="body"><h3>Support 24/24</h3>Lorem ipsum dolor sit<br>amit enuram ti adse</div>
</div>
<div class="abs feature" style="left:464px">
  <div style="font:400 38px/1 'Open Sans',sans-serif;width:30px;text-align:center">?</div>
  <div class="body"><h3>Question's</h3>fact that a reader will<br>be distracted by the</div>
</div>
<div class="abs feature" style="left:651px;align-items:flex-start;padding-top:14px">
  <div style="flex:1">
    <h3 style="text-align:center;margin-bottom:8px">Newsletter</h3>
    <div style="display:flex;gap:8px;align-items:center">
      <svg width="29" height="21" viewBox="0 0 29 21"><rect x="1" y="1" width="27" height="19" fill="#fff" stroke="#222"/><path d="M1 1l13.5 11L28 1M1 20l10-10M28 20L18 10" fill="none" stroke="#222" stroke-width="1.3"/></svg>
      <div class="newsletter-field" style="flex:1;margin:0"><i></i><b><svg width="18" height="17" viewBox="0 0 18 17"><path d="M7 5l5 3.5L7 12z" fill="#fff"/></svg></b></div>
    </div>
  </div>
</div>

<footer class="abs footer"></footer>
<div class="abs foot-col menu" style="left:90px"><h4>MENU</h4><ul>
  <li class="hl">Home</li><li>Shop</li><li>The Latest</li><li>About Us</li><li>FAQ</li><li>Blog</li><li>Contact Us</li></ul></div>
<div class="abs foot-col" style="left:239px"><h4>CUSTOMER SERVICE</h4><ul><li>Contact Us</li><li>Returns</li><li>Site Map</li></ul></div>
<div class="abs foot-col" style="left:387px"><h4>EXTRAS</h4><ul><li>Brands</li><li>Gift Vouchers</li><li>Affiliates</li><li>Specials</li></ul></div>
<div class="abs foot-col" style="left:536px"><h4>MY ACCOUNT</h4><ul><li>My Account</li><li>Order History</li><li>Wish List</li><li>Newsletter</li></ul></div>
<div class="abs foot-col social" style="left:694px"><h4>FOLLOW US</h4><ul style="margin-top:4px">
  <li><i></i>Chatterpage</li><li><i></i>Chirpline</li><li><i></i>Orbnet+</li><li><i></i>Clipboardly</li><li><i></i>Vidstream</li></ul></div>

<div class="abs bottom-bar">
  <div class="copy">© 2014, <span>yoursite</span>, All rights reserved.</div>
  <div class="cards"><span>Mintcard</span><span>Amerivault</span><span>Vexa</span><span>PayPlume</span></div>
  <div class="seal" role="img" aria-label="Secure payment seal"></div>
</div>
</body>
</html>
```